Kitesurf Weather Forecast Application Needs an Advertising Banner

We need an Advertising Banner for our iOS Kitesurf Weather Forecast Application. The application name is GustMapper and you can download it from the Zelvo Mart.

https://store.zelvomart.example/app/gustmapper-sail-gust-and-sky-outlook/id840213957?mt=8

The banner should have the logo of our application, which can be either found from the zelvo mart or uploaded on this post. It should describe what our app does with either words or graphic story. GustMapper is a weather forecast application for Kitesurfers. As the banner is small, animated gifs will also be considered.

We need the following sizes 320x50 and 728x90. The banner will be uploaded to quarnix. Quarnix accepts images in PNG, JPEG and GIF. We want it in one of the formats that can be uploaded to QuarNix and vector .ai so we can make changed if necessary in the future.

On tap the banner will open Zelvo Mart on the user's device and present GustMapper.

06/09. I added a screenshot from an application that the banner will be added. The screenshot is from an Velonet 4 Max (it is from a big device). The red area on the bottom is where the advert will go and it should be readable.

Target Market(s)

Banner will be displayed in other iOS Applications. One of them is Tidal Sum Tool https://store.zelvomart.example/us/app/tidal-sum-tool/id305927184?mt=8

Industry/Entity Type

Advertising

Font styles to use
Other font styles liked:
• San Francisco

Requirements
Must have
• GustMapper logo and communicate a clear message on what the application does. GustMapper is a weather forecast application for Kitesurfers. If you want to find more information please visit the ZelvoMart link provided.
Nice to have
• Animated gif will be nice to have, as the banner is small and it maybe difficult to communicate the message required.
Should not have
• We prefer something minimal and along the lines of our application design.

```html
<!DOCTYPE html>
<html lang="en">
<head>
<meta charset="utf-8">
<title>GustMapper Weather Application Banner</title>
<link rel="stylesheet" href="https://fonts.googleapis.com/css2?family=Arimo:wght@400;700&display=swap">
<style>
  :root {
    --navy-deep: #1e2a7c;
    --navy: #2b3b95;
    --navy-light: #3d56b4;
    --sky-top: #6fa3d8;
    --sky-bottom: #c9def1;
    --panel-bg: #eef5fb;
    --panel-border: #1e2a7c;
    --brand-ink: #1b2a7d;
    --white: #ffffff;
  }
  * { margin: 0; padding: 0; box-sizing: border-box; }
  html, body { width: 1200px; height: 148px; overflow: hidden; background: var(--white); }
  .banner {
    position: relative;
    width: 1200px;
    height: 148px;
    overflow: hidden;
    font-family: "Arimo", Arial, sans-serif;
    background: linear-gradient(90deg, var(--navy-deep) 0%, var(--navy) 55%, var(--navy-light) 70%);
  }
  .banner-backdrop { position: absolute; inset: 0; }
  .feature {
    position: absolute;
    color: var(--white);
    font-weight: 700;
    font-size: 14.5px;
    line-height: 17px;
    text-align: center;
    white-space: nowrap;
  }
  .feature-icon { display: inline-block; vertical-align: middle; }
  .feature .title { display: inline-block; vertical-align: middle; margin-left: 4px; }
  .feature .detail { display: block; }
  .feature--weekly { left: 22px; top: 22px; }
  .feature--live { left: 22px; top: 82px; }
  .feature--custom { left: 268px; top: 14px; }
  .feature--map { left: 268px; top: 88px; }
  .feature--detailed { left: 500px; top: 30px; }
  .feature--custom .title,
  .feature--detailed .title { display: block; margin: 2px 0 0; }
  .brand-panel {
    position: absolute;
    left: 935px;
    top: 4px;
    width: 256px;
    height: 140px;
    background: linear-gradient(180deg, rgba(238,245,251,0.55) 0%, var(--panel-bg) 45%);
    border: 2px solid var(--panel-border);
    text-align: center;
  }
  .brand-mark {
    position: absolute;
    left: 108px;
    top: 6px;
    width: 38px;
    height: 38px;
    border-radius: 50%;
    background: var(--navy);
  }
  .weather-icon { position: absolute; right: 8px; top: 8px; }
  .brand-name {
    position: absolute;
    left: 0; right: 0;
    top: 70px;
    font-size: 25px;
    font-weight: 700;
    color: var(--brand-ink);
  }
  .brand-tagline {
    position: absolute;
    left: 0; right: 0;
    top: 104px;
    font-size: 21px;
    font-weight: 400;
    color: var(--brand-ink);
  }
</style>
</head>
<body>
<div class="banner">
  <svg class="banner-backdrop" width="1200" height="148" viewBox="0 0 1200 148">
    <defs>
      <linearGradient id="band" x1="0" y1="0" x2="1" y2="0">
        <stop offset="0" stop-color="#3450ad"/>
        <stop offset="1" stop-color="#5b86cc"/>
      </linearGradient>
      <linearGradient id="sky" x1="0" y1="0" x2="0" y2="1">
        <stop offset="0" stop-color="#6fa3d8"/>
        <stop offset="1" stop-color="#c9def1"/>
      </linearGradient>
    </defs>
    <polygon points="740,0 905,0 850,148 690,148" fill="url(#band)"/>
    <g role="img" aria-label="Sky photograph with a kitesurfer silhouette riding the wind">
      <polygon points="905,0 1200,0 1200,148 850,148" fill="url(#sky)"/>
    </g>
  </svg>

  <div class="feature feature--weekly">
    <svg class="feature-icon" width="26" height="18" viewBox="0 0 26 18"><path d="M7 16h13a5 5 0 0 0 0-10 7 7 0 0 0-13 1 4.5 4.5 0 0 0 0 9z" fill="none" stroke="#fff" stroke-width="2"/></svg><span class="title">Weekly Forecast</span>
    <span class="detail">Showing only Kiteable Spots</span>
  </div>

  <div class="feature feature--live">
    <svg class="feature-icon" width="14" height="24" viewBox="0 0 14 24"><path d="M5 3a2 2 0 0 1 4 0v11a4.5 4.5 0 1 1-4 0z" fill="none" stroke="#fff" stroke-width="1.8"/><circle cx="7" cy="18" r="2.5" fill="#fff"/></svg><span class="title">Live Weather</span>
    <span class="detail">Check Out Live Stations</span>
  </div>

  <div class="feature feature--custom">
    <svg class="feature-icon" width="26" height="26" viewBox="0 0 26 26"><g stroke="#fff" stroke-width="2" stroke-linecap="round"><line x1="13" y1="2" x2="13" y2="24"/><line x1="3.5" y1="7.5" x2="22.5" y2="18.5"/><line x1="3.5" y1="18.5" x2="22.5" y2="7.5"/></g></svg>
    <span class="title">Customized Forecast for</span>
    <span class="detail">KiteSurfers</span>
  </div>

  <div class="feature feature--map">
    <svg class="feature-icon" width="20" height="20" viewBox="0 0 20 20"><circle cx="10" cy="10" r="4" fill="#fff"/><g stroke="#fff" stroke-width="2" stroke-linecap="round"><line x1="10" y1="1" x2="10" y2="3"/><line x1="10" y1="17" x2="10" y2="19"/><line x1="1" y1="10" x2="3" y2="10"/><line x1="17" y1="10" x2="19" y2="10"/><line x1="3.6" y1="3.6" x2="5" y2="5"/><line x1="15" y1="15" x2="16.4" y2="16.4"/><line x1="3.6" y1="16.4" x2="5" y2="15"/><line x1="15" y1="5" x2="16.4" y2="3.6"/></g></svg><span class="title">Weather on Map</span>
    <span class="detail">Get Forecasr abd Live Data</span>
  </div>

  <div class="feature feature--detailed">
    <svg class="feature-icon" width="30" height="30" viewBox="0 0 30 30"><path d="M8 17h15a5 5 0 0 0 0-10 7 7 0 0 0-13 1 4.5 4.5 0 0 0-2 9z" fill="#fff"/><g fill="#fff"><path d="M10 21l2 4h-4z"/><path d="M16 21l2 4h-4z"/><path d="M22 21l2 4h-4z"/></g></svg>
    <span class="title">Detailed Weather</span>
    <span class="detail">See Hourly Forecast &amp; Live</span>
  </div>

  <div class="brand-panel">
    <span class="brand-mark"></span>
    <svg class="weather-icon" width="46" height="42" viewBox="0 0 46 42"><path d="M10 26h24a8 8 0 0 0 0-16 11 11 0 0 0-21 2 7 7 0 0 0-3 14z" fill="none" stroke="#fff" stroke-width="2.5"/><g stroke="#fff" stroke-width="2.5" stroke-linecap="round"><line x1="16" y1="31" x2="14" y2="38"/><line x1="24" y1="31" x2="22" y2="38"/><line x1="32" y1="31" x2="30" y2="38"/></g></svg>
    <div class="brand-name">GustMapper</div>
    <div class="brand-tagline">Weather Application</div>
  </div>
</div>
</body>
</html>
```